Real Estate Search Site Re-Design of 2 Pages

Looking for designs to optimize 2 pages of our current site design. Our site allows users to find properties to purchase or rent.

Basically there are 4 panes
1. The top red one where you actually type in what you''re looking for.
2. The map pane that shows the properties
3. The scrollable results pane.
4. Property details pane.

A typical search would go like this:
1. User fills in their search criteria in the top pane in red. Clicks Find Homes
2. Site updates the map with properties plotted that fit the criteria. Site also populates the results pane at the bottom. Site shows the most newest property that fits the search criteria on the right.
3. User will scroll through the results pane or the map and click a property.
4. Site will update the property details pane with information on the selected property.

Search/Results Page
This main page needs a search form area, a results area, an area to display details of a property selected, a map to show results, and an area to display a real estate agent's information. The design must be full-screen to use all the space on the screen. All information should fit on a 1366x768 screen size. Please see sample screen shot.

Property Details Page
This one can be fixed width of 978px. This page needs all the elements that are displayed in the sample PNG file. Ideally, we want to be able to see all important information without scrolling on a 1366x768 screen. The important information in this size are Pictures with controls, address, bedrooms, bathrooms, square feet, square feet of the lot, days on market, agent information, and buttons to request a showing or get more information.

Our Goal:
Our goal is to get create a different way to display the data in an effective way. We want different ways to show the search results, maybe a vertical, scrolling list of property information with pictures. Or even a horizontal scrolling results pane. It must contain:

1. A map of the results
2. A way to scroll through the search results (like we have currently in case someone wants to search/sort bedrooms or square footage)
3. A way to view details of the property
4. A way to display agent information/picture
Updates

There's a lot of good design work coming through. Thank you.

Perhaps review some other real estate sales sites for ideas on pane configuration. Example site links:
http://www.brovat.example/homes/for_sale/?gclid=QXmP7k2-tb9DHR4W1KzeqN5BCE (brovat.example)
http://www.pemnox.example/?sem=3.4.2.6.8.2.1.15&gclid=RJwz82m-tb9DHWcn4KzeuTpBHS (Pemnox.example)
http://www.quindert.example/map_search/results/i/ (quindert.example)

Our goal for the redesign is to display the data in a more effective way. Either with a better flow, more pictures, more information, smoother search process. Please see the updated brief for details. The main idea is to show the data in the most effective way possible.

Project Deadline Extended
Reason: Still looking at different ideas for the search results. We are still open for fresh ideas.

Industry/Entity Type

Real Estate

Font styles to use
Sans Serif

Colors
eb1f27

```html
<!DOCTYPE html>
<html lang="en">
<head>
<meta charset="utf-8">
<title>Property Search</title>
<link href="https://fonts.googleapis.com/css2?family=Lato:wght@400;700&display=swap" rel="stylesheet">
<style>
:root{
  --brand:#eb1f27;
  --brand-dark:#b5121a;
  --accent:#c4222a;
  --pin:#c8232b;
  --ink:#222;
  --muted:#8a8a8a;
  --line:#dcdcdc;
  --panel:#f2f2f2;
  --map:#e6e0d3;
  --map-soft:#ddd7c8;
  --bar:rgba(40,40,40,.82);
  --photo-sky:#9fb7c9;
  --photo-green:#5d7a3f;
}
*{box-sizing:border-box;margin:0;padding:0}
html,body{width:1200px;height:884px;overflow:hidden;font-family:"Lato",sans-serif;color:var(--ink);background:#fff}
.app{position:relative;width:1200px;height:884px;overflow:hidden}
.topbar{position:absolute;left:0;top:0;width:1200px;height:65px;background:var(--brand);color:#fff}
.brand{position:absolute;left:16px;top:15px;font-size:26px;font-weight:700;letter-spacing:.2px}
.brand span{font-weight:400}
.search{position:absolute;left:227px;top:17px;width:209px;height:31px;background:#fff;border-radius:16px;display:flex;align-items:center;padding-left:12px;font-size:15px;color:#aaa}
.search svg{margin-right:10px}
.filters{position:absolute;left:445px;top:17px;height:31px;display:flex}
.filter{display:flex;align-items:center;padding:0 9px;border-left:1px solid rgba(255,255,255,.35);font-size:14px;font-weight:700;gap:6px}
.filter .caret{width:0;height:0;border-left:4px solid transparent;border-right:4px solid transparent;border-top:5px solid #fff}
.save{position:absolute;left:888px;top:15px;width:96px;height:34px;background:var(--brand-dark);border-radius:3px;font-size:14px;display:flex;align-items:center;justify-content:center}
.lang{position:absolute;right:13px;top:26px;font-size:11px;letter-spacing:.2px}
.lang u{text-decoration:underline}

.map{position:absolute;left:0;top:65px;width:703px;height:819px;background:linear-gradient(160deg,var(--map) 0%,var(--map-soft) 50%,var(--map) 100%)}
.map-pins{position:absolute;left:0;top:0;width:703px;height:884px;pointer-events:none}
.map-bar{position:absolute;left:0;top:65px;width:703px;height:36px;background:var(--bar);color:#fff;font-size:13px;font-weight:700;display:flex;align-items:center;justify-content:space-between;padding:0 18px}
.map-bar em{font-style:italic;font-weight:400}
.sort{display:flex;align-items:center;gap:14px}
.grid-toggle{position:absolute;left:651px;top:466px;width:52px;height:70px;background:var(--accent);border-radius:35px 0 0 35px;display:flex;align-items:center;justify-content:center;padding-left:6px}

.results{position:absolute;left:703px;top:65px;width:147px;height:819px;background:var(--panel);box-shadow:inset 3px 0 4px rgba(0,0,0,.15)}
.card{height:141px;text-align:center;padding-top:11px}
.thumb{width:115px;height:71px;margin:0 auto;border:1px solid #bbb;padding:2px;background:#fff}
.thumb-img{position:relative;width:100%;height:100%;background:linear-gradient(var(--photo-sky) 0,#8fa7a0 45%,var(--photo-green) 100%)}
.thumb-nav{position:absolute;left:0;right:0;bottom:0;height:10px;background:rgba(0,0,0,.75);color:#fff;font-size:6px;line-height:10px}
.price{font-size:14px;font-weight:700;margin-top:6px}
.meta{font-size:10px;font-weight:700;margin-top:5px}
.meta b{color:var(--accent)}
.addr{font-size:10px;color:var(--accent);margin-top:4px}
.scroll{position:absolute;top:65px;width:17px;height:819px;background:#f4f4f4;border-left:1px solid var(--line)}
.scroll .thumbbar{position:absolute;left:3px;top:14px;width:11px;height:56px;background:#c6c6c6;border-radius:2px}

.details{position:absolute;left:867px;top:65px;width:316px;height:819px;background:#fff}
.title{position:absolute;left:21px;top:15px;font-size:16.5px;font-weight:400;color:var(--accent);line-height:21px}
.photo{position:absolute;left:21px;top:71px;width:271px;height:184px;border:1px solid #bbb;padding:5px}
.photo-img{position:relative;width:100%;height:100%;background:linear-gradient(var(--photo-sky) 0,#8aa59a 45%,var(--photo-green) 100%)}
.photo-nav{position:absolute;left:0;right:0;bottom:0;height:26px;background:linear-gradient(transparent,rgba(0,0,0,.55));color:#fff;font-size:13px;display:flex;align-items:center;justify-content:space-between;padding:0 6px}
.list-price{position:absolute;left:23px;top:267px;font-size:17px}
.list-price b{font-weight:700}
.beds{position:absolute;left:25px;top:297px;font-size:13.5px}
.sqft{position:absolute;left:25px;top:330px;font-size:13.5px;font-weight:700;color:var(--accent)}
.lot{position:absolute;left:25px;top:360px;font-size:13.5px;font-weight:700;color:var(--muted)}
.dom{position:absolute;left:26px;top:391px;font-size:13px}
.courtesy{position:absolute;left:27px;top:419px;font-size:13px}
.btn{position:absolute;top:450px;height:30px;border-radius:3px;font-size:13px;display:flex;align-items:center;justify-content:center}
.btn-ghost{left:28px;width:90px;background:#ccc;color:#333}
.btn-primary{left:126px;width:90px;background:var(--accent);color:#fff}
.divider{position:absolute;left:0;top:500px;width:316px;height:1px;background:var(--line)}
.agent-photo{position:absolute;left:12px;top:518px;width:113px;height:138px;border:1px solid #bbb;padding:3px}
.agent-photo div{width:100%;height:100%;background:linear-gradient(#d9dfe4,#8fb0c6)}
.agent{position:absolute;left:138px;top:517px;font-size:14.5px;line-height:24.5px}
.agent .name{color:var(--accent);font-weight:700;font-size:15.5px}
.agent .mail{color:var(--accent)}
.field{position:absolute;left:12px;width:282px;height:32px;border:1px solid #ccc;font-size:14px;color:#bbb;padding:7px 8px;white-space:nowrap;overflow:hidden}
</style>
</head>
<body>
<div class="app">
  <header class="topbar">
    <div class="brand">Company <span>Name</span></div>
    <div class="search">
      <svg width="16" height="16" viewBox="0 0 16 16" aria-hidden="true"><circle cx="6.5" cy="6.5" r="5" fill="none" stroke="#999" stroke-width="2"/><line x1="10.2" y1="10.2" x2="15" y2="15" stroke="#999" stroke-width="2.4" stroke-linecap="round"/></svg>
      Alhambra
    </div>
    <nav class="filters">
      <div class="filter">$50K - $75K<span class="caret"></span></div>
      <div class="filter" style="padding-left:12px">3+ Beds<span class="caret" style="margin-left:8px"></span></div>
      <div class="filter">Home Type<span class="caret"></span></div>
      <div class="filter">Baths<span class="caret" style="margin-left:8px"></span></div>
      <div class="filter">More<span class="caret"></span></div>
    </nav>
    <div class="save">Save Search</div>
    <div class="lang">LANGUAGE : <u>ENGLISH</u> &nbsp;|&nbsp; CHINESE</div>
  </header>

  <section class="map" role="img" aria-label="Street map of the search area"></section>
  <svg class="map-pins" viewBox="0 0 703 884" aria-label="Property markers on the map" role="img">
    <defs>
      <symbol id="pin-condo" viewBox="0 0 24 30">
        <path d="M12 29 6 22H3a3 3 0 0 1-3-3V3a3 3 0 0 1 3-3h18a3 3 0 0 1 3 3v16a3 3 0 0 1-3 3h-3z" fill="var(--pin)"/>
        <rect x="7" y="4" width="10" height="14" fill="#fff"/>
        <rect x="9" y="6" width="2" height="2" fill="var(--pin)"/><rect x="13" y="6" width="2" height="2" fill="var(--pin)"/>
        <rect x="9" y="10" width="2" height="2" fill="var(--pin)"/><rect x="13" y="10" width="2" height="2" fill="var(--pin)"/>
        <rect x="11" y="14" width="2" height="4" fill="var(--pin)"/>
      </symbol>
      <symbol id="pin-house" viewBox="0 0 24 30">
        <path d="M12 29 6 22H3a3 3 0 0 1-3-3V3a3 3 0 0 1 3-3h18a3 3 0 0 1 3 3v16a3 3 0 0 1-3 3h-3z" fill="var(--pin)"/>
        <path d="M12 3 3 11h3v7h12v-7h3z" fill="#fff"/>
        <rect x="10" y="12" width="4" height="6" fill="var(--pin)"/>
      </symbol>
    </defs>
    <use href="#pin-condo" x="99" y="125" width="22" height="27"/>
    <use href="#pin-condo" x="401" y="78" width="22" height="27"/>
    <use href="#pin-condo" x="620" y="188" width="22" height="27"/>
    <use href="#pin-condo" x="331" y="237" width="22" height="27"/>
    <use href="#pin-house" x="388" y="239" width="22" height="27"/>
    <use href="#pin-condo" x="366" y="284" width="22" height="27"/>
    <use href="#pin-condo" x="28" y="284" width="22" height="27"/>
    <use href="#pin-condo" x="64" y="330" width="22" height="27"/>
    <use href="#pin-condo" x="549" y="348" width="22" height="27"/>
    <use href="#pin-house" x="606" y="349" width="22" height="27"/>
    <use href="#pin-condo" x="584" y="394" width="22" height="27"/>
    <use href="#pin-condo" x="378" y="420" width="22" height="27"/>
    <use href="#pin-condo" x="282" y="440" width="22" height="27"/>
    <use href="#pin-condo" x="409" y="553" width="22" height="27"/>
    <use href="#pin-condo" x="107" y="599" width="22" height="27"/>
    <use href="#pin-condo" x="627" y="663" width="22" height="27"/>
    <use href="#pin-condo" x="339" y="713" width="22" height="27"/>
    <use href="#pin-house" x="396" y="715" width="22" height="27"/>
    <use href="#pin-condo" x="373" y="760" width="22" height="27"/>
    <use href="#pin-condo" x="36" y="760" width="22" height="27"/>
    <use href="#pin-condo" x="72" y="805" width="22" height="27"/>
    <use href="#pin-condo" x="556" y="823" width="22" height="27"/>
    <use href="#pin-house" x="613" y="825" width="22" height="27"/>
    <use href="#pin-condo" x="592" y="864" width="22" height="27"/>
  </svg>
  <div class="map-bar">
    <span>58 Properties found</span>
    <span class="sort"><em>Sort : </em>Price
      <svg width="12" height="20" viewBox="0 0 12 20" aria-hidden="true"><path d="M6 1 11 8H1z M6 19 1 12h10z" fill="#fff"/></svg>
    </span>
  </div>
  <div class="grid-toggle">
    <svg width="28" height="28" viewBox="0 0 28 28" aria-hidden="true" fill="#fff">
      <rect x="0" y="0" width="7" height="7"/><rect x="10" y="0" width="7" height="7"/><rect x="20" y="0" width="7" height="7"/>
      <rect x="0" y="10" width="7" height="7"/><rect x="10" y="10" width="7" height="7"/><rect x="20" y="10" width="7" height="7"/>
      <rect x="0" y="20" width="7" height="7"/><rect x="10" y="20" width="7" height="7"/><rect x="20" y="20" width="7" height="7"/>
    </svg>
  </div>

  <aside class="results">
    <article class="card"><div class="thumb"><div class="thumb-img" role="img" aria-label="Front view of a two-storey house"><div class="thumb-nav">‹ &nbsp; 1/32 &nbsp; ›</div></div></div><div class="price">$23,388,000</div><div class="meta">3 bd &nbsp;|&nbsp; 3 ba &nbsp;|&nbsp; <b>3640 sf</b></div><div class="addr">812 Corvell Lane, Ma...</div></article>
    <article class="card"><div class="thumb"><div class="thumb-img" role="img" aria-label="Front view of a two-storey house"><div class="thumb-nav">‹ &nbsp; 1/32 &nbsp; ›</div></div></div><div class="price">$23,388,000</div><div class="meta">3 bd &nbsp;|&nbsp; 3 ba &nbsp;|&nbsp; <b>3640 sf</b></div><div class="addr">812 Corvell Lane, Ma...</div></article>
    <article class="card"><div class="thumb"><div class="thumb-img" role="img" aria-label="Front view of a two-storey house"><div class="thumb-nav">‹ &nbsp; 1/32 &nbsp; ›</div></div></div><div class="price">$23,388,000</div><div class="meta">3 bd &nbsp;|&nbsp; 3 ba &nbsp;|&nbsp; <b>3640 sf</b></div><div class="addr">812 Corvell Lane, Ma...</div></article>
    <article class="card"><div class="thumb"><div class="thumb-img" role="img" aria-label="Front view of a two-storey house"><div class="thumb-nav">‹ &nbsp; 1/32 &nbsp; ›</div></div></div><div class="price">$23,388,000</div><div class="meta">3 bd &nbsp;|&nbsp; 3 ba &nbsp;|&nbsp; <b>3640 sf</b></div><div class="addr">812 Corvell Lane, Ma...</div></article>
    <article class="card"><div class="thumb"><div class="thumb-img" role="img" aria-label="Front view of a two-storey house"><div class="thumb-nav">‹ &nbsp; 1/32 &nbsp; ›</div></div></div><div class="price">$23,388,000</div><div class="meta">3 bd &nbsp;|&nbsp; 3 ba &nbsp;|&nbsp; <b>3640 sf</b></div><div class="addr">812 Corvell Lane, Ma...</div></article>
    <article class="card"><div class="thumb"><div class="thumb-img" role="img" aria-label="Front view of a two-storey house"><div class="thumb-nav">‹ &nbsp; 1/32 &nbsp; ›</div></div></div><div class="price">$23,388,000</div><div class="meta">3 bd &nbsp;|&nbsp; 3 ba &nbsp;|&nbsp; <b>3640 sf</b></div><div class="addr">812 Corvell Lane, Ma...</div></article>
  </aside>
  <div class="scroll" style="left:850px"><div class="thumbbar"></div></div>

  <section class="details">
    <h1 class="title">812 Corvell Lane<br>Maple Grove</h1>
    <div class="photo"><div class="photo-img" role="img" aria-label="Front view of the selected two-storey house with lawn and trees">
      <div class="photo-nav">
        <svg width="10" height="16" viewBox="0 0 10 16" aria-hidden="true"><path d="M8 1 2 8l6 7" fill="none" stroke="#fff" stroke-width="1.6"/></svg>
        <span>1/32</span>
        <svg width="10" height="16" viewBox="0 0 10 16" aria-hidden="true"><path d="M2 1l6 7-6 7" fill="none" stroke="#fff" stroke-width="1.6"/></svg>
      </div>
    </div></div>
    <div class="list-price"><b>$23,388,000</b> Listing Price</div>
    <div class="beds"><b>3 Beds, 3 Baths</b>, Built in 2014</div>
    <div class="sqft">3640 sqft</div>
    <div class="lot">9,866 sqft lot</div>
    <div class="dom">25 days on market (#AR5520918)</div>
    <div class="courtesy">Courtesy of Halden Crest Realty</div>
    <div class="btn btn-ghost">View Details</div>
    <div class="btn btn-primary">Visit Home</div>
    <div class="divider"></div>
    <div class="agent-photo"><div role="img" aria-label="Portrait photo of the buyer's agent"></div></div>
    <div class="agent">
      Buyer's Agent<br>
      <span class="name">Mira Castell</span><br>
      (626) 555-0148<br>
      <span class="mail">mira@haldencrest.example</span><br>
      BRE #02958341
    </div>
    <div class="field" style="top:673px">Your Name</div>
    <div class="field" style="top:718px">Phone</div>
    <div class="field" style="top:762px">Email</div>
    <div class="field" style="top:807px">I am interested in 812 Corvell Lane</div>
  </section>
  <div class="scroll" style="left:1183px"><div class="thumbbar"></div></div>
</div>
</body>
</html>
```